International Clinical Software Company needs a new business card design

We are looking for a new business card design for our company that has recently expanded into the UK market, making us a multinational company.
After having rebranded our website and produced a new style guide, we are looking for a business card that is creative and attention grabbing, while being consistent with the style and colour scheme used on the new website, www.brookvale.example
We produce care management technology for the aged care market, but the main aspect we aim to communicate is the human element of our software, and the way it assists in providing better care for aged people, and stronger relationships between aged people and the staff that care for them.
Our current business card is a dark green with gold text, which makes the text quite difficult to read, not very aesthetically appealing and the colour scheme looks quite dated.
We would like something fresh and modern, that can still be colourful but doesn't use large blocks of dark colour, and uses the colours within our logo.
Something tying in with the leaves that are used in our logo could work quite nicely, along with the Autumn/Fall colours of soft greens, yellows and reds (also in our existing logo). However also happy to look at fresh, completely out of the box ideas we may not have yet considered.
Target Market(s)
The people that receive this business card work in the aged card or health industry and are either corporate/management level staff or clinical (Registered Nurses, care workers etc.)
Industry/Entity Type
Health Product
Contact Information for Business Card
Company Name - BrookvaleTech
Company locations: United Kingdom, Australia, New Zealand
Staff Details:
Staff name: Dermot Quill
Staff job title: Executive Chairman
Staff email: d.quill@brookvale.example
Office phone number: 01632 960418
Font styles to use
Other font styles liked:
- Calibri
Requirements
Must have
- Must include the BrookvaleTech brand name in it's current font
- Must include logo (3 leaves in gold circle)
- Must include Business Card Details
Nice to have
- Elements of gold
- White space
- Something autumn themed but not too cliched
Should not have
- No blue - used by a major competitor and we would like to differentiate from them
- Large blocks of dark green colour (the green that appears in our leaves on the logo on our current business card is the background colour and it is far too dark)

```html
<!DOCTYPE html>
<html lang="en">
<head>
<meta charset="utf-8">
<title>BrookvaleTech Business Card</title>
<link rel="stylesheet" href="https://fonts.googleapis.com/css2?family=Open+Sans:wght@400;600&display=swap">
<style>
  :root {
    --backdrop: #3b424c;
    --card: #ffffff;
    --gold: #b89b2c;
    --tan: #b59d6c;
    --ink: #1f1f1f;
    --tree-top: #c6a83a;
    --tree-bottom: #ad8f22;
  }
  html, body {
    margin: 0;
    width: 1200px;
    height: 960px;
    overflow: hidden;
    background: var(--backdrop);
    font-family: "Open Sans", Arial, sans-serif;
  }
  .card {
    position: absolute;
    left: 100px;
    top: 194px;
    width: 1000px;
    height: 572px;
    background: var(--card);
    border-radius: 34px;
    overflow: hidden;
  }
  .brand {
    position: absolute;
    left: 110px;
    top: 40px;
    display: flex;
    flex-direction: column;
    align-items: center;
  }
  .brand-mark {
    width: 170px;
    height: 170px;
    border-radius: 50%;
    background: var(--tan);
  }
  .brand-name {
    margin-top: 16px;
    font-size: 44px;
    font-weight: 400;
    color: var(--tan);
    letter-spacing: 1px;
  }
  .contact {
    position: absolute;
    left: 90px;
    top: 320px;
    margin: 0;
    padding: 0;
    list-style: none;
    font-size: 22px;
    line-height: 1.35;
    color: var(--ink);
  }
  .contact li {
    display: flex;
    align-items: flex-start;
    gap: 12px;
    margin-bottom: 4px;
  }
  .contact svg {
    width: 22px;
    height: 22px;
    flex: none;
    margin-top: 4px;
    fill: var(--gold);
  }
  .person {
    position: absolute;
    left: 640px;
    top: 270px;
  }
  .person-name {
    margin: 0;
    font-size: 40px;
    font-weight: 600;
    color: var(--gold);
    letter-spacing: 1px;
  }
  .person-title {
    margin: 2px 0 0;
    font-size: 22px;
    color: var(--ink);
    letter-spacing: 0.5px;
  }
  .tree-art {
    position: absolute;
    left: 700px;
    top: 390px;
    width: 260px;
    height: 182px;
    background: linear-gradient(180deg, var(--tree-top), var(--tree-bottom));
    opacity: 0.85;
    border-radius: 8px 8px 0 0;
  }
</style>
</head>
<body>
  <div class="card">
    <div class="brand">
      <div class="brand-mark"></div>
      <div class="brand-name">BrookvaleTech</div>
    </div>

    <ul class="contact">
      <li>
        <svg viewBox="0 0 24 24" aria-hidden="true"><path d="M6.6 10.8a15.1 15.1 0 0 0 6.6 6.6l2.2-2.2c.3-.3.7-.4 1-.2 1.1.4 2.3.6 3.6.6.6 0 1 .4 1 1V20c0 .6-.4 1-1 1A17 17 0 0 1 3 4c0-.6.4-1 1-1h3.5c.6 0 1 .4 1 1 0 1.3.2 2.5.6 3.6.1.3 0 .7-.2 1z"/></svg>
        <span>01632 960418</span>
      </li>
      <li>
        <svg viewBox="0 0 24 24" aria-hidden="true"><path d="M2 5h20v14H2z M3.5 6.5 12 13l8.5-6.5" fill-rule="evenodd"/><path d="M3 6l9 7 9-7" fill="none" stroke="#fff" stroke-width="1.5"/></svg>
        <span>d.quill@brookvale.example</span>
      </li>
      <li>
        <svg viewBox="0 0 24 24" aria-hidden="true"><path d="M12 3 2 12h3v8h5v-5h4v5h5v-8h3z"/></svg>
        <span>BrookvaleTech<br>United Kingdom, Australia, New Zealand</span>
      </li>
    </ul>

    <div class="person">
      <h1 class="person-name">Dermot Quill</h1>
      <p class="person-title">Executive Chairman</p>
    </div>

    <div class="tree-art" role="img" aria-label="Gold illustration of a bare autumn tree with a small round sun beside it"></div>
  </div>
</body>
</html>
```